Price Trend Graphic for Estimates

I want to add a graphic to my estimates that shows the projected price trend of the work we are quoting to the customer. I have attached a couple ideas I was working on but they are garbage. Hopefully you can see the intent and make it look a lot better. Basically I want the customer to see a really a professional / technological graphic that will stimulate them to purchase Right Now! before the price goes up further. So maybe if the "Today's Price" looks nice and friendly and then becomes more critical and ominous as it goes forward 30 days.... 90 days.... Idea is to psychologically

Target Market(s)

Customers for our Construction business

Industry/Entity Type

Construction

Colors
0054AA
0677BA
7BADD7
CADEEF
E8F1F8
0094D4
00A9DD
6FCCEA
C7EBF8
E9F6FB
FFF300
FFF600
FEFA6F
FFFEC7
FFFEE8
F0912C
F2A743
F7CA91
FBE8D2
FDF5EE

Requirements
Must have
• nice looking graphic with upwards moving arrow and 3 price points
Nice to have
• technological / modern looking chart

```html
<!DOCTYPE html>
<html lang="en">
<head>
<meta charset="utf-8">
<title>Estimated Price Trend</title>
<link href="https://fonts.googleapis.com/css2?family=Montserrat:wght@300;400;800&display=swap" rel="stylesheet">
<style>
  :root {
    --bg: #d7eef8;
    --navy: #1c456b;
    --grid: #8aafc8;
    --teal: #007a70;
    --orange: #f15a29;
    --red: #be1e2d;
    --ring: #fff200;
    --white: #ffffff;
    --fill-top: #eea654;
    --fill-mid: #eed55c;
    --fill-low: #e2e9b4;
    --fill-base: #d7eef8;
  }
  * { margin: 0; padding: 0; box-sizing: border-box; }
  html, body { width: 1200px; height: 849px; overflow: hidden; background: var(--bg); }
  .canvas { position: relative; width: 1200px; height: 849px; font-family: 'Montserrat', sans-serif; }
  .heading { position: absolute; left: 70px; top: 54px; }
  .heading-kicker {
    display: block; margin-left: 27px;
    font-weight: 300; font-size: 25px; letter-spacing: 7px;
    color: var(--navy); line-height: 1;
  }
  .heading-pill {
    position: relative; margin-top: 6px; width: 328px; height: 36px;
    border: 1.5px solid var(--navy); border-radius: 18px; overflow: hidden;
    display: flex; align-items: center;
  }
  .heading-pill::after {
    content: ""; position: absolute; left: 216px; top: 0; right: 0; bottom: 0;
    background: var(--navy);
  }
  .heading-title {
    margin-left: 25px; font-weight: 800; font-size: 25px;
    color: var(--navy); line-height: 1; letter-spacing: 0.3px;
  }
  .chart { position: absolute; left: 0; top: 0; }
  .price { font-family: 'Montserrat', sans-serif; font-weight: 800; font-size: 27px; text-anchor: middle; }
  .label { font-family: 'Montserrat', sans-serif; font-weight: 400; font-size: 14px; text-anchor: middle; letter-spacing: 0.5px; }
</style>
</head>
<body>
<div class="canvas">
  <div class="heading">
    <span class="heading-kicker">ESTIMATED</span>
    <div class="heading-pill"><span class="heading-title">PRICE TREND</span></div>
  </div>

  <svg class="chart" width="1200" height="849" viewBox="0 0 1200 849" aria-label="Price trend chart rising from today to 60 days">
    <defs>
      <linearGradient id="area-fill" x1="0" y1="228" x2="0" y2="750" gradientUnits="userSpaceOnUse">
        <stop offset="0" stop-color="var(--fill-top)"/>
        <stop offset="0.4" stop-color="var(--fill-mid)"/>
        <stop offset="0.7" stop-color="var(--fill-low)"/>
        <stop offset="1" stop-color="var(--fill-base)"/>
      </linearGradient>
      <path id="pin" d="M -87 5 C -87 -46 -46 -87 0 -87 C 46 -87 87 -46 87 5 C 87 48 32 124 0 168 C -32 124 -87 48 -87 5 Z"/>
    </defs>

    <polygon class="area" points="222,566 485.5,528 750,453 1014,229 1014,750 222,750" fill="url(#area-fill)"/>

    <g class="grid" stroke="var(--grid)" stroke-width="1.2" opacity="0.85">
      <line x1="221" y1="200.7" x2="1014" y2="200.7"/>
      <line x1="221" y1="256.6" x2="1014" y2="256.6"/>
      <line x1="221" y1="312.5" x2="1014" y2="312.5"/>
      <line x1="221" y1="368.4" x2="1014" y2="368.4"/>
      <line x1="221" y1="424.4" x2="1014" y2="424.4"/>
      <line x1="221" y1="480.3" x2="1014" y2="480.3"/>
      <line x1="221" y1="536.2" x2="1014" y2="536.2"/>
      <line x1="221" y1="592.1" x2="1014" y2="592.1"/>
      <line x1="221" y1="648" x2="1014" y2="648"/>
      <line x1="221" y1="703.9" x2="1014" y2="703.9"/>
      <line x1="221" y1="173" x2="221" y2="750"/>
      <line x1="485.5" y1="173" x2="485.5" y2="750"/>
      <line x1="750" y1="173" x2="750" y2="750"/>
      <line x1="1014" y1="173" x2="1014" y2="750"/>
    </g>

    <g class="trend" fill="none" stroke="var(--navy)" stroke-width="5" stroke-linejoin="round">
      <polyline points="222,566 485.5,528 750,453 1036,209"/>
    </g>
    <polygon class="arrow-head" points="1023,200 1049,195.5 1041,220.5" fill="var(--navy)"/>

    <g class="node">
      <circle cx="222" cy="566" r="19" fill="var(--navy)"/><circle cx="222" cy="566" r="11.5" fill="var(--teal)"/>
      <circle cx="485.5" cy="528" r="19" fill="var(--navy)"/><circle cx="485.5" cy="528" r="11.5" fill="var(--orange)"/>
      <circle cx="750" cy="453" r="19" fill="var(--navy)"/><circle cx="750" cy="453" r="11.5" fill="var(--red)"/>
    </g>

    <g class="pin pin-today" transform="translate(222,349)">
      <use href="#pin" fill="var(--teal)"/>
      <circle r="75" fill="none" stroke="var(--ring)" stroke-width="2.2"/>
      <circle r="66" fill="var(--bg)"/>
      <text class="price" y="9" fill="var(--teal)">$6,500</text>
      <text class="label" y="27" fill="var(--teal)">Today price</text>
    </g>

    <g class="pin pin-30" transform="translate(485.5,314)">
      <use href="#pin" fill="var(--orange)"/>
      <circle r="75" fill="none" stroke="var(--ring)" stroke-width="2.2"/>
      <circle r="66" fill="var(--bg)"/>
      <text class="price" y="9" fill="var(--orange)">$7,280</text>
      <text class="label" y="27" fill="var(--orange)">30 Days Price</text>
    </g>

    <g class="pin pin-60" transform="translate(750,232.5)">
      <use href="#pin" fill="var(--red)"/>
      <circle r="75" fill="none" stroke="var(--ring)" stroke-width="2.2"/>
      <circle r="66" fill="var(--bg)"/>
      <text class="price" y="9" fill="var(--red)">$7,460</text>
      <text class="label" y="27" fill="var(--red)">60 Days Price</text>
    </g>
  </svg>
</div>
</body>
</html>
```